Plastic Surgeon Stationary Design

I Already have the logo. I Want and a clean, minimalist and elegant project. Please, I prefer Black, White and Gold color but you're free to try another ones. Business card,
Letterhead (A4 and Office), Recipes (Letter Pad) (A5), Envelop, Invoice, Computer Bill, Bill Book, Single A4 page size,
You Have to create at least the same materials I already own. I would like to a file to use in word to print letterheads and letter pad.
What I want that you make more changes are the envelopes that are to colorful and not elegant.
I'll not accept any design without my addresses as you can guide yourself with the models I provide.
Here are the addresses too:
"www.clevandrotavares.example" (website)
(My clinics' address)
"SÃO PAULO
Rua Heitor Lunardi, 1870, Lunardi Corporate, Cj 204
São Paulo - SP
(11) 98432-6120"
"BALNEÁRIO CAMBORIÚ
Rua Benedito Kauer, 418, 7° andar
Edificio Vale Azul
Balneário Camboriú - SC
(047) 9246-3180"
Attention: Letterheads, Recipes, have to contain "CRM/SC 27.583 and CRM/SP 238.416" close to my name (Dr. Clevandro Tavares - Cirurgião Plástico), it is usually placed at the bottom.
Designers, attention!
During the process of creating bear in mind that the details of the logo, as the faces on the sides, are designed to be subtle. Highlight other such details affect the delicacy and elegance of the logo and visual identity.
When you are creating stationery, do not abuse the use of the logo, it should be used once or at most two times in each item.
Remember! Each stationery set must submit 3 models, one with the address "Balneario Camboriu", another with the address of "São Paulo" and the third containing both addresses.
The model letter envelope, folder type bag for letterhead and folder with inner pocket that provided a model did not please me because they are very flashy. Give preference to the use of white or black background.
PLEASE! Seek inspiration in the models contained in this link:
https://www.filecrate.example/sh/kq27pz58wnr4c1v/MbTyLo_QaZ
In this link you can find my PAST Stationary Itens, so it can help you on your work
https://stashbin.example/8RkLQ2vNm3TeHwYz
Reason: Nobody presented anything useful.
Reason: still waiting some designers send their projects
Reason: Still Waiting Some Designs....
Target Market(s)
Mostly females with good economical condition. (Class A and AB)
Industry/Entity Type
Business
Requirements
Must have
- You have to provide 3 models of each paper, one with the address of São Paulo, another with the Balneario Camboriú address, and the third one with both addresses.

```html
<!DOCTYPE html>
<html lang="pt-BR">
<head>
<meta charset="utf-8">
<title>Dr. Clevandro Tavares – Cartão de Visita</title>
<link rel="stylesheet" href="https://fonts.googleapis.com/css2?family=Arimo:wght@400;700&family=Playfair+Display:wght@700&display=swap">
<style>
  :root {
    --backdrop: #e4e4e4;
    --card-top: #414347;
    --card-bottom: #2b2d30;
    --band: #2f3134;
    --band-line: #46484c;
    --white: #f4f4f4;
    --gold: #c2916b;
    --muted: #85878b;
  }
  * { margin: 0; padding: 0; box-sizing: border-box; }
  html, body { width: 1200px; height: 1200px; overflow: hidden; }
  body {
    background: var(--backdrop);
    position: relative;
    font-family: "Arimo", Arial, sans-serif;
  }
  .card {
    position: absolute;
    top: 210px;
    width: 440px;
    height: 780px;
    background: linear-gradient(180deg, var(--card-top) 0%, var(--card-bottom) 100%);
    box-shadow: 0 14px 34px rgba(0,0,0,0.28);
    overflow: hidden;
    text-align: center;
  }
  .card--front { left: 130px; }
  .card--back { left: 630px; }

  .brand-mark {
    display: flex;
    align-items: center;
    justify-content: center;
    gap: 10px;
    color: var(--white);
  }
  .brand-mark__dot {
    width: 10px; height: 10px;
    border-radius: 50%;
    background: var(--white);
  }
  .card--front .brand-mark {
    margin-top: 112px;
    font-size: 15px;
    font-weight: 700;
    letter-spacing: 0.04em;
  }
  .doctor-name {
    margin-top: 62px;
    color: var(--white);
    font-weight: 700;
    font-size: 20px;
    letter-spacing: 0.05em;
  }
  .doctor-title {
    margin-top: 8px;
    color: var(--gold);
    font-size: 16px;
  }
  .clinics {
    margin-top: 128px;
    color: var(--muted);
    font-size: 16px;
    line-height: 1.3;
    letter-spacing: 0.02em;
  }
  .clinic + .clinic { margin-top: 20px; }
  .website {
    position: absolute;
    left: 0; right: 0;
    top: 560px;
    color: var(--gold);
    font-size: 16px;
    letter-spacing: 0.05em;
  }
  .gold-rule {
    position: absolute;
    left: 0; right: 0;
    height: 5px;
    background: var(--gold);
  }
  .pattern-band {
    position: absolute;
    left: 0; right: 0; bottom: 0;
    background: linear-gradient(180deg, var(--band) 0%, #292b2e 100%);
  }
  .card--front .gold-rule { top: 614px; }
  .card--front .pattern-band { top: 619px; }

  .card--back .lockup {
    position: absolute;
    left: 0; right: 0;
    top: 300px;
  }
  .card--back .brand-mark {
    font-family: "Playfair Display", Georgia, serif;
    font-weight: 700;
    font-size: 38px;
  }
  .card--back .brand-mark__dot { width: 12px; height: 12px; }
  .tagline {
    margin-top: 10px;
    color: var(--gold);
    font-size: 13px;
    letter-spacing: 0.42em;
    text-transform: uppercase;
  }
  .card--back .gold-rule { top: 610px; }
  .card--back .pattern-band { top: 615px; }
</style>
</head>
<body>
  <section class="card card--front" aria-label="Frente do cartão">
    <div class="brand-mark"><span class="brand-mark__dot"></span>Clevandro Tavares</div>
    <h1 class="doctor-name">DR. CLEVANDRO TAVARES</h1>
    <p class="doctor-title">Cirurgião Plástico</p>
    <div class="clinics">
      <p class="clinic">BALNEÁRIO CAMBORIÚ - SC<br>(47) 9246 3180</p>
      <p class="clinic">SÃO PAULO - SP<br>(11) 98432 6120</p>
    </div>
    <p class="website">CLEVANDROTAVARES.EXAMPLE</p>
    <div class="gold-rule"></div>
    <div class="pattern-band" role="img" aria-label="Faixa com padrão decorativo de círculos entrelaçados em cinza"></div>
  </section>

  <section class="card card--back" aria-label="Verso do cartão">
    <div class="lockup">
      <div class="brand-mark"><span class="brand-mark__dot"></span>Clevandro Tavares</div>
      <p class="tagline">Cirurgia Plástica</p>
    </div>
    <div class="gold-rule"></div>
    <div class="pattern-band" role="img" aria-label="Faixa com padrão decorativo de círculos entrelaçados em cinza"></div>
  </section>
</body>
</html>
```